Powerpoint design for Halvora Trade Allies

We would like to have a Power point template/design with flexibilities and good opportunities to do changes.
• Be able to change in image background
• Themes are HTA colors and complementary colors. Please come with suggestions.
• Alternate white and blue background
• Standard functions and opportunities within Powerpoint should be able to be used or be accessible.
• Feel free to change/alter the logo for example remove or separate the text in the logo ("Halvora Trade Allies" ) and the tagline ("Partners in lasting growth")
• www.halvoratradeallies.se

```html
<!DOCTYPE html>
<html lang="en">
<head>
<meta charset="utf-8">
<title>Halvora Trade Allies – Presentation Template</title>
<link href="https://fonts.googleapis.com/css2?family=Libre+Baskerville&family=Open+Sans:wght@400;600;700;800&display=swap" rel="stylesheet">
<style>
:root{
  --navy:#123f86;
  --navy-dark:#0c2f66;
  --blue:#3f6fb5;
  --sky:#7ea7dc;
  --green:#7cc242;
  --green-light:#b5e08c;
  --grey:#8a8a8a;
  --grey-light:#e6e6e6;
  --page:#eeeeee;
  --text:#6f6f6f;
}
*{margin:0;padding:0;box-sizing:border-box}
html,body{width:1200px;height:3375px;overflow:hidden;background:var(--page);font-family:'Open Sans',sans-serif}
.canvas{position:relative;width:1200px;height:3375px}
.hero{position:absolute;width:560px;height:316px}
.hero>.slide{position:absolute;left:0;top:0;transform:scale(1.4894);transform-origin:0 0}
.slide{position:absolute;width:376px;height:212px;background:#fff;overflow:hidden;box-shadow:0 1px 4px rgba(0,0,0,.14);color:var(--text)}
.slide.blue{background:var(--navy);color:#fff}
.t{position:absolute;left:14px;top:10px;font:400 12.5px 'Libre Baskerville',serif;color:var(--navy);white-space:nowrap}
.blue .t{color:#fff}
.st{position:absolute;left:14px;top:27px;font:600 4.5px 'Open Sans',sans-serif;color:#8a8a8a;letter-spacing:.3px;text-transform:uppercase}
.blue .st{color:#d7e2f3}
.mark{position:absolute;right:12px;top:9px;font:800 14px 'Open Sans',sans-serif;color:var(--navy);letter-spacing:-.3px}
.blue .mark{color:#fff}
.foot{position:absolute;left:12px;right:12px;bottom:5px;font:400 3.4px 'Open Sans',sans-serif;color:#999;border-bottom:1.5px solid var(--navy);padding-bottom:2px;display:flex;justify-content:space-between}
.blue .foot{color:#c9d6ea;border-color:#fff}
.p{position:absolute;font:400 4px/1.55 'Open Sans',sans-serif;color:var(--text)}
.blue .p{color:#dfe7f4}
.h{font:700 4.6px 'Libre Baskerville',serif;color:var(--navy);margin-bottom:2px}
.blue .h{color:#fff}
.ph{position:absolute}
.faint{position:absolute;font:800 120px 'Open Sans',sans-serif;color:#f3f3f3;letter-spacing:-4px;white-space:nowrap}
.blue .faint{color:#17478f}
.brand{position:absolute;text-align:center;color:var(--navy)}
.brand b{display:block;font:800 30px 'Open Sans',sans-serif;letter-spacing:-1px;line-height:1}
.brand span{display:block;font:600 11px 'Open Sans',sans-serif;margin-top:3px}
.brand i{display:block;font-style:normal;font:600 5.5px 'Open Sans',sans-serif;letter-spacing:1.6px;margin-top:2px}
.dots{position:absolute;display:flex;gap:2px}
.dots span{width:5px;height:5px;border-radius:50%;border:.8px solid currentColor}
.btn{display:inline-block;margin-top:5px;background:var(--blue);color:#fff;font:600 3.6px 'Open Sans',sans-serif;padding:2px 7px;border-radius:2px}
.num{position:absolute;font:400 22px 'Libre Baskerville',serif;color:#dcdcdc}
.list-row{position:absolute;left:236px;width:126px;border-bottom:.6px solid #ddd;padding:3px 0 3px;font:600 4.5px 'Open Sans',sans-serif;color:#333;display:flex;align-items:center;gap:5px}
.list-row i{width:7px;height:7px;border-radius:50%;background:var(--navy);flex:none}
.cap{position:absolute;font:600 4px 'Open Sans',sans-serif;color:#fff;text-align:center}
table.tc{position:absolute;border-collapse:collapse;font:400 3.6px 'Open Sans',sans-serif;color:#777}
table.tc td,table.tc th{padding:3px 4px;text-align:center;border-bottom:.6px solid #e4e4e4}
table.tc th{color:#fff;font-weight:700}
.sheet{position:absolute;display:grid;grid-template-columns:repeat(8,1fr);border-left:.5px solid #ccc;border-top:.5px solid #ccc}
.sheet span{height:7px;border-right:.5px solid #ccc;border-bottom:.5px solid #ccc;font:400 3px 'Open Sans',sans-serif;color:#555;padding-left:1px}
.logo-box{position:absolute;width:46px;height:20px;background:#fff;border:.6px solid #e2e2e2;box-shadow:0 1px 2px rgba(0,0,0,.08)}
.logo-box::after{content:"";position:absolute;left:12px;top:7px;width:22px;height:6px;background:#d7d7d7;border-radius:1px}
.sw{position:absolute;width:34px;height:28px}
</style>
</head>
<body>
<div class="canvas">

<!-- ============ FEATURED SLIDES ============ -->
<div class="hero" style="left:30px;top:50px">
  <div class="slide">
    <div class="ph" role="img" aria-label="Strip of business photos: desk work, hands with tablet, network graphics" style="left:0;top:0;width:376px;height:132px;background:linear-gradient(90deg,#e6a650,#d9893a 20%,#5e5048 45%,#2c3f57 65%,#8c8f96 85%,#cfd2d6)"></div>
    <div class="ph" style="left:0;top:132px;width:376px;height:80px;background:#f1f1f1"></div>
    <div class="mark" style="left:22px;top:165px;right:auto;font-size:15px">HTA</div>
    <div style="position:absolute;left:72px;top:160px;width:1px;height:26px;background:#bbb"></div>
    <div style="position:absolute;left:84px;top:162px;font:400 10px 'Libre Baskerville',serif;color:var(--navy)">Halvora Trade Allies Template</div>
    <div style="position:absolute;left:84px;top:177px;font:400 4.5px 'Open Sans',sans-serif;color:#888">Month 2021</div>
  </div>
</div>

<div class="hero" style="left:610px;top:50px">
  <div class="slide">
    <div class="t">Agenda</div>
    <div class="ph" role="img" aria-label="Portrait of a smiling businessman in shirt and tie" style="left:20px;top:50px;width:150px;height:162px;background:linear-gradient(180deg,#dfe4ec,#b8c3d6 60%,#8ea0bd)"></div>
    <div class="p" style="left:210px;top:58px;width:140px">
      <div class="h" style="font-family:'Open Sans',sans-serif">Agenda Text 1</div>Simple text about the first topic to cover.<br><br>
      <div class="h" style="font-family:'Open Sans',sans-serif">Agenda Text 2</div>Simple text about the second topic to cover.<br><br>
      <div class="h" style="font-family:'Open Sans',sans-serif">Agenda Text 3</div>Simple text about the third topic to cover.<br><br>
      <div class="h" style="font-family:'Open Sans',sans-serif">Agenda Text 4</div>Simple text about the fourth topic to cover.
    </div>
  </div>
</div>

<div class="hero" style="left:30px;top:420px">
  <div class="slide blue">
    <div class="faint" style="left:150px;top:20px">HTA</div>
    <div class="t">Your Title Here</div>
    <div class="st">Subtitle Goes Here</div>
    <div class="mark">HTA</div>
    <div class="p" style="left:14px;top:52px;width:120px">
      <div class="h">Content Here</div>You can simply impress your audience and add a unique zing and appeal to your presentations. Easy to change colors, photos and text. Get a modern presentation that is beautifully designed and simple to edit.
      <br><span class="btn">Learn More</span>
    </div>
    <div class="ph" role="img" aria-label="Laptop on a white desk with coffee cup" style="left:160px;top:62px;width:180px;height:100px;background:linear-gradient(135deg,#f4f4f4,#d9d9d9);border:4px solid #2a2a2a;border-radius:4px"></div>
    <div class="foot"><span>© Copyright Halvora Trade Allies | All Rights Reserved</span><span>PAGE | 10</span></div>
  </div>
</div>

<div class="hero" style="left:610px;top:420px">
  <div class="slide">
    <div class="t">Timeline</div>
    <div class="st">Subtitle Goes Here</div>
    <div class="mark">HTA</div>
    <div style="position:absolute;left:14px;top:96px;font:400 7px 'Open Sans',sans-serif;color:#333">Start<br><span style="font-size:4px;color:#888">Contents</span></div>
    <svg style="position:absolute;left:0;top:0" width="376" height="212">
      <line x1="40" y1="106" x2="340" y2="106" stroke="#c9d6ea" stroke-width="1.5"/>
      <g fill="var(--sky)"><circle cx="70" cy="106" r="5"/><circle cx="112" cy="106" r="5"/></g>
      <g fill="var(--blue)"><circle cx="154" cy="106" r="5"/><circle cx="196" cy="106" r="5"/></g>
      <g fill="var(--navy)"><circle cx="238" cy="106" r="5"/><circle cx="280" cy="106" r="5"/></g>
      <circle cx="320" cy="106" r="9" fill="var(--green)"/>
      <text x="320" y="107.5" font-size="4" fill="#fff" text-anchor="middle" font-family="Open Sans">2021</text>
      <g font-size="4" fill="#555" text-anchor="middle" font-family="Open Sans">
        <text x="70" y="96">2013</text><text x="112" y="120">2014</text><text x="154" y="96">2016</text>
        <text x="196" y="120">2018</text><text x="238" y="96">2019</text><text x="280" y="120">2020</text>
      </g>
      <text x="320" y="92" font-size="4.5" fill="var(--green)" text-anchor="middle" font-family="Open Sans">Vision</text>
    </svg>
    <div class="p" style="left:48px;top:130px;width:280px;display:flex;justify-content:space-around;text-align:center"><span style="width:50px">Contents<br>Short text fits here</span><span style="width:50px">Contents<br>Short text fits here</span><span style="width:50px">Contents<br>Short text fits here</span></div>
    <div class="p" style="left:48px;top:52px;width:280px;display:flex;justify-content:space-around;text-align:center"><span style="width:50px">Contents<br>Short text fits here</span><span style="width:50px">Contents<br>Short text fits here</span><span style="width:50px">Contents<br>Short text fits here</span></div>
    <div class="foot"><span>© Copyright Halvora Trade Allies | All Rights Reserved</span><span>PAGE | 11</span></div>
  </div>
</div>

<div class="hero" style="left:30px;top:790px">
  <div class="slide">
    <div class="t">Table Of Content</div>
    <div class="mark">HTA</div>
    <div class="num" style="left:20px;top:44px">1</div><div class="num" style="left:20px;top:92px">2</div><div class="num" style="left:20px;top:140px">3</div>
    <div class="num" style="left:190px;top:44px">4</div><div class="num" style="left:190px;top:92px">5</div><div class="num" style="left:190px;top:140px">6</div>
    <div class="p" style="left:44px;top:52px;width:120px"><div class="h">Content here</div>Get a modern presentation that is easy to change.</div>
    <div class="p" style="left:44px;top:100px;width:120px"><div class="h">Content here</div>Get a modern presentation that is easy to change.</div>
    <div class="p" style="left:44px;top:148px;width:120px"><div class="h">Content here</div>Get a modern presentation that is easy to change.</div>
    <div class="p" style="left:214px;top:52px;width:120px"><div class="h">Content here</div>Get a modern presentation that is easy to change.</div>
    <div class="p" style="left:214px;top:100px;width:120px"><div class="h">Content here</div>Get a modern presentation that is easy to change.</div>
    <div class="p" style="left:214px;top:148px;width:120px"><div class="h">Content here</div>Get a modern presentation that is easy to change.</div>
    <div class="foot"><span>© Copyright Halvora Trade Allies | All Rights Reserved</span><span>PAGE | 8</span></div>
  </div>
</div>

<div class="hero" style="left:610px;top:790px">
  <div class="slide">
    <div class="faint" style="left:40px;top:30px;font-size:150px">HTA</div>
    <div class="brand" style="left:0;right:0;top:62px"><b>HTA</b><span>Halvora Trade Allies</span><i>Partners in lasting growth</i></div>
  </div>
</div>

<!-- ============ SLIDE GRID ============ -->
<!-- row 1 -->
<div class="slide" style="left:14px;top:1238px">
  <div class="faint" style="left:20px;top:10px">HTA</div>
  <div class="brand" style="left:0;right:0;top:60px"><b>HTA</b><span>Halvora Trade Allies</span><i>Partners in lasting growth</i></div>
  <div style="position:absolute;right:6px;top:60px;writing-mode:vertical-rl;font:400 3.5px 'Open Sans',sans-serif;color:#aaa">www.halvoratradeallies.se</div>
</div>
<div class="slide" style="left:407px;top:1238px">
  <div class="mark" style="left:36px;top:78px;right:auto;font-size:42px;letter-spacing:-1.5px">HTA</div>
  <div style="position:absolute;left:190px;top:22px;width:1px;height:170px;background:#ccc"></div>
  <div style="position:absolute;left:204px;top:38px;font:400 15px/1.15 'Libre Baskerville',serif;color:var(--navy)">Master Slide<br>Presentation</div>
  <div class="p" style="left:204px;top:80px">Subtitle Goes Here</div>
  <div class="dots" style="left:204px;top:176px;color:var(--navy)"><span></span><span></span><span></span><span></span></div>
</div>
<div class="slide blue" style="left:800px;top:1238px">
  <div class="mark" style="left:36px;top:78px;right:auto;font-size:42px;letter-spacing:-1.5px">HTA</div>
  <div style="position:absolute;left:190px;top:22px;width:1px;height:170px;background:#5677ad"></div>
  <div style="position:absolute;left:204px;top:38px;font:400 15px/1.15 'Libre Baskerville',serif">Master Slide<br>Presentation</div>
  <div class="p" style="left:204px;top:80px">Subtitle Goes Here</div>
  <div class="dots" style="left:204px;top:176px;color:#fff"><span></span><span></span><span></span><span></span></div>
</div>

<!-- row 2 -->
<div class="slide" style="left:14px;top:1476px">
  <div class="mark" style="left:0;right:0;top:8px;text-align:center;font-size:18px">HTA</div>
  <div class="ph" role="img" aria-label="Dimmed business photo under a blue overlay" style="left:0;top:40px;width:376px;height:172px;background:linear-gradient(180deg,#1e4a8e,#123f86)"></div>
  <div style="position:absolute;left:0;right:0;top:68px;text-align:center;font:400 4px 'Open Sans',sans-serif;color:#d8e2f2">www.halvoratradeallies.se</div>
  <div style="position:absolute;left:0;right:0;top:110px;text-align:center;font:400 15px 'Libre Baskerville',serif;color:#fff">HTA Master Slide Template</div>
  <div style="position:absolute;left:0;right:0;top:130px;text-align:center;font:600 4px 'Open Sans',sans-serif;letter-spacing:2px;color:#d8e2f2">SUBTITLE GOES HERE</div>
  <div style="position:absolute;left:0;right:0;top:150px;text-align:center;font:400 4px 'Open Sans',sans-serif;color:#d8e2f2">Month 2021</div>
  <div class="dots" style="left:174px;top:186px;color:#fff"><span></span><span></span><span></span><span></span></div>
</div>
<div class="slide" style="left:407px;top:1476px">
  <div class="ph" role="img" aria-label="Strip of business photos: desk work, hands with tablet, network graphics" style="left:0;top:0;width:376px;height:132px;background:linear-gradient(90deg,#e6a650,#d9893a 20%,#5e5048 45%,#2c3f57 65%,#8c8f96 85%,#cfd2d6)"></div>
  <div class="ph" style="left:0;top:132px;width:376px;height:80px;background:#f1f1f1"></div>
  <div class="mark" style="left:22px;top:165px;right:auto;font-size:15px">HTA</div>
  <div style="position:absolute;left:72px;top:160px;width:1px;height:26px;background:#bbb"></div>
  <div style="position:absolute;left:84px;top:162px;font:400 10px 'Libre Baskerville',serif;color:var(--navy)">Halvora Trade Allies Template</div>
  <div style="position:absolute;left:84px;top:177px;font:400 4.5px 'Open Sans',sans-serif;color:#888">Month 2021</div>
</div>
<div class="slide" style="left:800px;top:1476px">
  <div class="t">Agenda</div>
  <div class="ph" role="img" aria-label="Portrait of a smiling businessman in shirt and tie" style="left:20px;top:50px;width:150px;height:162px;background:linear-gradient(180deg,#dfe4ec,#b8c3d6 60%,#8ea0bd)"></div>
  <div class="p" style="left:210px;top:48px;width:140px">
    <div class="h" style="font-family:'Open Sans',sans-serif">Agenda Text 1</div>Simple text about the first topic to cover.<br><br>
    <div class="h" style="font-family:'Open Sans',sans-serif">Agenda Text 2</div>Simple text about the second topic to cover.<br><br>
    <div class="h" style="font-family:'Open Sans',sans-serif">Agenda Text 3</div>Simple text about the third topic to cover.<br><br>
    <div class="h" style="font-family:'Open Sans',sans-serif">Agenda Text 4</div>Simple text about the fourth topic to cover.
  </div>
</div>

<!-- row 3 -->
<div class="slide" style="left:14px;top:1714px">
  <div class="ph" style="left:0;top:0;width:100px;height:212px;background:var(--navy)"></div>
  <div class="mark" style="left:14px;top:10px;right:auto;color:#fff;font-size:13px">HTA</div>
  <div style="position:absolute;left:14px;top:100px;width:16px;height:1px;background:#fff"></div>
  <div style="position:absolute;left:14px;top:106px;font:400 13px 'Libre Baskerville',serif;color:#fff">Agenda</div>
  <div style="position:absolute;left:14px;top:190px;font:400 3.6px 'Open Sans',sans-serif;color:#cfdaee">Add your text here</div>
  <div class="ph" role="img" aria-label="City skyline at night with a glowing network globe" style="left:100px;top:0;width:120px;height:212px;background:linear-gradient(180deg,#0c1a35,#1b3564 55%,#4b5f86)"></div>
  <div class="list-row" style="top:28px"><i></i>Introduction</div>
  <div class="list-row" style="top:55px"><i></i>About Us</div>
  <div class="list-row" style="top:82px"><i></i>Welcome Message</div>
  <div class="list-row" style="top:109px"><i></i>Our Services</div>
  <div class="list-row" style="top:136px"><i></i>Our Team</div>
  <div class="list-row" style="top:163px"><i></i>Contact Us</div>
</div>
<div class="slide" style="left:407px;top:1714px">
  <div class="t">Table Of Content</div>
  <div class="mark">HTA</div>
  <div class="num" style="left:20px;top:44px">1</div><div class="num" style="left:20px;top:92px">2</div><div class="num" style="left:20px;top:140px">3</div>
  <div class="num" style="left:190px;top:44px">4</div><div class="num" style="left:190px;top:92px">5</div><div class="num" style="left:190px;top:140px">6</div>
  <div class="p" style="left:44px;top:52px;width:120px"><div class="h">Content here</div>Get a modern presentation that is easy to change.</div>
  <div class="p" style="left:44px;top:100px;width:120px"><div class="h">Content here</div>Get a modern presentation that is easy to change.</div>
  <div class="p" style="left:44px;top:148px;width:120px"><div class="h">Content here</div>Get a modern presentation that is easy to change.</div>
  <div class="p" style="left:214px;top:52px;width:120px"><div class="h">Content here</div>Get a modern presentation that is easy to change.</div>
  <div class="p" style="left:214px;top:100px;width:120px"><div class="h">Content here</div>Get a modern presentation that is easy to change.</div>
  <div class="p" style="left:214px;top:148px;width:120px"><div class="h">Content here</div>Get a modern presentation that is easy to change.</div>
  <div class="foot"><span>© Copyright Halvora Trade Allies | All Rights Reserved</span><span>PAGE | 8</span></div>
</div>
<div class="slide" style="left:800px;top:1714px">
  <div class="faint" style="left:190px;top:60px;font-size:80px">HTA</div>
  <div class="t">Your Title Here</div>
  <div class="st">Subtitle Goes Here</div>
  <div class="mark">HTA</div>
  <div class="p" style="left:24px;top:58px;width:170px;text-align:center"><div class="h">Content Here</div>You can simply impress your audience and add a unique zing and appeal to your presentations. Get a modern presentation that is beautifully designed. Easy to change colors, photos and text in just a few clicks.</div>
  <div class="foot"><span>© Copyright Halvora Trade Allies | All Rights Reserved</span><span>PAGE | 9</span></div>
</div>

<!-- row 4 -->
<div class="slide blue" style="left:14px;top:1952px">
  <div class="faint" style="left:150px;top:20px">HTA</div>
  <div class="t">Your Title Here</div>
  <div class="st">Subtitle Goes Here</div>
  <div class="mark">HTA</div>
  <div class="p" style="left:14px;top:52px;width:120px">
    <div class="h">Content Here</div>You can simply impress your audience and add a unique zing and appeal to your presentations. Easy to change colors, photos and text. Get a modern presentation that is beautifully designed and simple to edit.
    <br><span class="btn">Learn More</span>
  </div>
  <div class="ph" role="img" aria-label="Laptop on a white desk with coffee cup" style="left:160px;top:62px;width:180px;height:100px;background:linear-gradient(135deg,#f4f4f4,#d9d9d9);border:4px solid #2a2a2a;border-radius:4px"></div>
  <div class="foot"><span>© Copyright Halvora Trade Allies | All Rights Reserved</span><span>PAGE | 10</span></div>
</div>
<div class="slide" style="left:407px;top:1952px">
  <div class="t">Timeline</div>
  <div class="st">Subtitle Goes Here</div>
  <div class="mark">HTA</div>
  <div style="position:absolute;left:14px;top:96px;font:400 7px 'Open Sans',sans-serif;color:#333">Start<br><span style="font-size:4px;color:#888">Contents</span></div>
  <svg style="position:absolute;left:0;top:0" width="376" height="212">
    <line x1="40" y1="106" x2="340" y2="106" stroke="#c9d6ea" stroke-width="1.5"/>
    <g fill="var(--sky)"><circle cx="70" cy="106" r="5"/><circle cx="112" cy="106" r="5"/></g>
    <g fill="var(--blue)"><circle cx="154" cy="106" r="5"/><circle cx="196" cy="106" r="5"/></g>
    <g fill="var(--navy)"><circle cx="238" cy="106" r="5"/><circle cx="280" cy="106" r="5"/></g>
    <circle cx="320" cy="106" r="9" fill="var(--green)"/>
    <text x="320" y="107.5" font-size="4" fill="#fff" text-anchor="middle" font-family="Open Sans">2021</text>
    <g font-size="4" fill="#555" text-anchor="middle" font-family="Open Sans">
      <text x="70" y="96">2013</text><text x="112" y="120">2014</text><text x="154" y="96">2016</text>
      <text x="196" y="120">2018</text><text x="238" y="96">2019</text><text x="280" y="120">2020</text>
    </g>
    <text x="320" y="92" font-size="4.5" fill="var(--green)" text-anchor="middle" font-family="Open Sans">Vision</text>
  </svg>
  <div class="p" style="left:48px;top:130px;width:280px;display:flex;justify-content:space-around;text-align:center"><span style="width:50px">Contents<br>Short text fits here</span><span style="width:50px">Contents<br>Short text fits here</span><span style="width:50px">Contents<br>Short text fits here</span></div>
  <div class="p" style="left:48px;top:52px;width:280px;display:flex;justify-content:space-around;text-align:center"><span style="width:50px">Contents<br>Short text fits here</span><span style="width:50px">Contents<br>Short text fits here</span><span style="width:50px">Contents<br>Short text fits here</span></div>
  <div class="foot"><span>© Copyright Halvora Trade Allies | All Rights Reserved</span><span>PAGE | 11</span></div>
</div>
<div class="slide" style="left:800px;top:1952px">
  <div class="t">Your Title Here</div>
  <div class="st">Subtitle Goes Here</div>
  <div class="mark">HTA</div>
  <svg style="position:absolute;left:18px;top:55px" width="110" height="110" viewBox="0 0 110 110">
    <circle cx="55" cy="55" r="50" fill="var(--navy)"/>
    <path d="M55 55 L55 5 A50 50 0 0 0 5 55 Z" fill="var(--blue)"/>
    <text x="58" y="68" font-family="Open Sans" font-weight="700" font-size="34" fill="#fff" text-anchor="middle">75<tspan font-size="16" dy="-14">%</tspan></text>
  </svg>
  <div class="p" style="left:150px;top:50px;width:210px"><div class="h">Content Title Here</div>Get a clean and modern presentation that is beautifully designed. Easy to change colors, photos and text.</div>
  <svg style="position:absolute;left:150px;top:88px" width="210" height="90">
    <g stroke="#eee" stroke-width=".6"><line x1="0" y1="10" x2="210" y2="10"/><line x1="0" y1="30" x2="210" y2="30"/><line x1="0" y1="50" x2="210" y2="50"/><line x1="0" y1="70" x2="210" y2="70"/></g>
    <rect x="14" y="12" width="8" height="68" fill="var(--navy)"/><rect x="48" y="38" width="8" height="42" fill="var(--navy)"/>
    <rect x="82" y="30" width="8" height="50" fill="var(--navy)"/><rect x="116" y="14" width="8" height="66" fill="var(--navy)"/>
    <rect x="150" y="40" width="8" height="40" fill="var(--navy)"/><rect x="184" y="62" width="8" height="18" fill="var(--green)"/>
    <line x1="0" y1="80" x2="210" y2="80" stroke="#bbb" stroke-width=".6"/>
    <g font-family="Open Sans" font-size="3.5" fill="#888" text-anchor="middle"><text x="18" y="87">Category 1</text><text x="52" y="87">Category 2</text><text x="86" y="87">Category 3</text><text x="120" y="87">Category 4</text><text x="154" y="87">Category 5</text><text x="188" y="87">Category 6</text></g>
  </svg>
  <div class="foot"><span>© Copyright Halvora Trade Allies | All Rights Reserved</span><span>PAGE | 12</span></div>
</div>

<!-- row 5 -->
<div class="slide" style="left:14px;top:2190px">
  <div class="t">Your Title Here</div>
  <div class="st">Subtitle Goes Here</div>
  <div class="mark">HTA</div>
  <div class="ph" role="img" aria-label="Classroom with desks and a large window" style="left:18px;top:50px;width:110px;height:60px;border-radius:4px;background:linear-gradient(180deg,#c5cdd9,#5a6f93)"></div>
  <div class="cap" style="left:18px;top:98px;width:110px;font-family:'Libre Baskerville',serif">Your Text Here</div>
  <div class="p" style="left:142px;top:52px;width:220px"><div class="h">Content Title Here</div>Get a clean and modern presentation that is beautifully designed. Easy to change colors, photos and text. You can simply impress your audience.</div>
  <div class="p" style="left:18px;top:128px;width:220px"><div class="h">Content Title Here</div>Get a clean and modern presentation that is beautifully designed. Easy to change colors, photos and text. You can simply impress your audience.</div>
  <div class="ph" role="img" aria-label="Hand writing on a document with a pen" style="left:252px;top:126px;width:110px;height:60px;border-radius:4px;background:linear-gradient(180deg,#dfe5ee,#6f86ad)"></div>
  <div class="cap" style="left:252px;top:174px;width:110px;font-family:'Libre Baskerville',serif">Your Text Here</div>
  <div class="foot"><span>© Copyright Halvora Trade Allies | All Rights Reserved</span><span>PAGE | 13</span></div>
</div>
<div class="slide" style="left:407px;top:2190px">
  <div class="t">Your Title Here</div>
  <div class="st">Subtitle Goes Here</div>
  <div class="mark">HTA</div>
  <div class="ph" role="img" aria-label="City skyline with a glowing network overlay" style="left:18px;top:62px;width:175px;height:100px;border-radius:4px;background:linear-gradient(180deg,#b6c6dc,#4e6c96 60%,#243a60)"></div>
  <svg style="position:absolute;left:0;top:0" width="376" height="212">
    <circle cx="196" cy="92" r="9" fill="var(--navy)"/><circle cx="196" cy="130" r="9" fill="var(--green)"/><circle cx="26" cy="153" r="4" fill="none" stroke="#fff" stroke-width=".8"/>
    <path d="M192 92 l3 3 l5 -6" stroke="#fff" stroke-width="1" fill="none"/><path d="M192 130 l3 3 l5 -6" stroke="#fff" stroke-width="1" fill="none"/>
  </svg>
  <div class="cap" style="left:32px;top:151px;text-align:left">Content Title Here</div>
  <div class="p" style="left:212px;top:84px;width:150px"><div class="h" style="font-size:4px">Content Title Here</div>Get a clean and modern presentation. Easy to change colors, photos and text.</div>
  <div class="p" style="left:212px;top:122px;width:150px"><div class="h" style="font-size:4px;color:var(--green)">Content Title Here</div>Get a clean and modern presentation. Easy to change colors, photos and text.</div>
  <div class="foot"><span>© Copyright Halvora Trade Allies | All Rights Reserved</span><span>PAGE | 14</span></div>
</div>
<div class="slide" style="left:800px;top:2190px">
  <div class="t">Pie Charts</div>
  <div class="st">Subtitle Goes Here</div>
  <div class="mark">HTA</div>
  <div class="p" style="left:60px;top:46px;width:256px;text-align:center">Get a clean and modern presentation that is beautifully designed. Easy to change colors, photos and text. You can simply impress your audience.</div>
  <svg style="position:absolute;left:0;top:70px" width="376" height="70" viewBox="0 0 376 70">
    <g fill="none" stroke-width="5">
      <circle cx="92" cy="35" r="16" stroke="#e4e4e4"/><circle cx="92" cy="35" r="16" stroke="var(--navy)" stroke-dasharray="68.3 100.5" transform="rotate(-90 92 35)"/>
      <circle cx="188" cy="35" r="16" stroke="#e4e4e4"/><circle cx="188" cy="35" r="16" stroke="var(--green)" stroke-dasharray="35.2 100.5" transform="rotate(-90 188 35)"/>
      <circle cx="284" cy="35" r="16" stroke="#e4e4e4"/><circle cx="284" cy="35" r="16" stroke="#9a9a9a" stroke-dasharray="55.3 100.5" transform="rotate(-90 284 35)"/>
    </g>
    <g font-family="Open Sans" font-weight="700" font-size="9" text-anchor="middle"><text x="92" y="38" fill="var(--navy)">68%</text><text x="188" y="38" fill="var(--green)">35%</text><text x="284" y="38" fill="#777">55%</text></g>
  </svg>
  <div class="p" style="left:62px;top:146px;width:60px;text-align:center">Get a clean and modern presentation that is beautifully designed</div>
  <div class="p" style="left:158px;top:146px;width:60px;text-align:center">Get a clean and modern presentation that is beautifully designed</div>
  <div class="p" style="left:254px;top:146px;width:60px;text-align:center">Get a clean and modern presentation that is beautifully designed</div>
  <div class="foot"><span>© Copyright Halvora Trade Allies | All Rights Reserved</span><span>PAGE | 15</span></div>
</div>

<!-- row 6 -->
<div class="slide" style="left:14px;top:2428px">
  <div class="ph" role="img" aria-label="Person writing in a notebook at a desk" style="left:0;top:0;width:140px;height:90px;background:linear-gradient(135deg,#b9c2cc,#56647a)"></div>
  <div class="ph" style="left:0;top:90px;width:140px;height:122px;background:var(--navy)"></div>
  <svg style="position:absolute;left:12px;top:80px" width="22" height="22"><circle cx="11" cy="11" r="10" fill="var(--blue)"/><text x="11" y="17" font-family="Libre Baskerville" font-size="13" fill="#fff" text-anchor="middle">“</text></svg>
  <div class="p" style="left:14px;top:110px;width:115px;color:#dfe7f4">Get a clean and modern presentation that is beautifully designed. Easy to change colors, photos and text. You can simply impress your audience.<br><br>– Team Name</div>
  <div class="mark">HTA</div>
  <div style="position:absolute;left:154px;top:50px;font:400 12px 'Libre Baskerville',serif;color:var(--navy)">Your Title Here</div>
  <div class="p" style="left:154px;top:68px;width:205px">Get a clean and modern presentation that is beautifully designed. Easy to change colors, photos and text in just a few clicks.</div>
  <svg style="position:absolute;left:158px;top:96px" width="8" height="90"><g fill="var(--navy)"><circle cx="4" cy="5" r="3"/><circle cx="4" cy="29" r="3" fill="var(--green)"/><circle cx="4" cy="53" r="3"/><circle cx="4" cy="77" r="3" fill="var(--green)"/></g></svg>
  <div class="p" style="left:172px;top:98px;width:180px;line-height:1.4">Get a clean and modern layout that is easy to edit.<br><br>Get a clean and modern layout that is easy to edit.<br><br>Get a clean and modern layout that is easy to edit.<br><br>Get a clean and modern layout that is easy to edit.</div>
  <div class="foot" style="left:150px"><span>© Copyright Halvora Trade Allies | All Rights Reserved</span><span>PAGE | 16</span></div>
</div>
<div class="slide" style="left:407px;top:2428px">
  <div class="faint" style="left:16px;top:40px;font-size:100px">HTA</div>
  <div class="brand" style="left:180px;width:150px;top:24px"><b style="font-size:20px">HTA</b><span style="font-size:7px">Halvora Trade Allies</span><i style="font-size:3.6px">Partners in lasting growth</i></div>
  <div style="position:absolute;left:212px;top:132px;font:400 12px 'Libre Baskerville',serif;color:var(--navy)">Section Title</div>
  <div class="p" style="left:212px;top:152px;width:130px">Get a clean and modern presentation that is easy to edit. Change colors, photos and text.</div>
</div>
<div class="slide blue" style="left:800px;top:2428px">
  <div class="faint" style="left:16px;top:40px;font-size:100px">HTA</div>
  <div class="brand" style="left:180px;width:150px;top:24px;color:#fff"><b style="font-size:20px">HTA</b><span style="font-size:7px">Halvora Trade Allies</span><i style="font-size:3.6px">Partners in lasting growth</i></div>
  <div style="position:absolute;left:212px;top:132px;font:400 12px 'Libre Baskerville',serif;color:#fff">Section Title</div>
  <div class="p" style="left:212px;top:152px;width:130px">Get a clean and modern presentation that is easy to edit. Change colors, photos and text.</div>
</div>

<!-- row 7 -->
<div class="slide" style="left:14px;top:2666px">
  <div class="t">Your Title Here</div>
  <div class="st">Subtitle Goes Here</div>
  <div class="mark">HTA</div>
  <div class="ph" role="img" aria-label="Team member portrait" style="left:30px;top:50px;width:70px;height:74px;background:linear-gradient(180deg,#d9d3cc,#8e7f72)"></div>
  <div class="ph" role="img" aria-label="Team member portrait" style="left:110px;top:50px;width:70px;height:74px;background:linear-gradient(180deg,#e7e2de,#a8423f)"></div>
  <div class="ph" role="img" aria-label="Team member portrait" style="left:190px;top:50px;width:70px;height:74px;background:linear-gradient(180deg,#e4e4e4,#6b5a52)"></div>
  <div class="ph" role="img" aria-label="Team member portrait" style="left:270px;top:50px;width:70px;height:74px;background:linear-gradient(180deg,#dedede,#3d3a3a)"></div>
  <div class="cap" style="left:30px;top:124px;width:70px;background:var(--navy);padding:2px 0">Member Name</div>
  <div class="cap" style="left:110px;top:124px;width:70px;background:var(--green);padding:2px 0">Member Name</div>
  <div class="cap" style="left:190px;top:124px;width:70px;background:var(--navy);padding:2px 0">Member Name</div>
  <div class="cap" style="left:270px;top:124px;width:70px;background:var(--navy);padding:2px 0">Member Name</div>
  <div class="p" style="left:30px;top:140px;width:310px;display:flex;justify-content:space-between;text-align:center"><span style="width:70px">Get a modern presentation that is well designed</span><span style="width:70px">Get a modern presentation that is well designed</span><span style="width:70px">Get a modern presentation that is well designed</span><span style="width:70px">Get a modern presentation that is well designed</span></div>
  <div class="dots" style="left:55px;top:170px;color:var(--navy)"><span></span><span></span><span></span></div>
  <div class="dots" style="left:135px;top:170px;color:var(--navy)"><span></span><span></span><span></span></div>
  <div class="dots" style="left:215px;top:170px;color:var(--navy)"><span></span><span></span><span></span></div>
  <div class="dots" style="left:295px;top:170px;color:var(--navy)"><span></span><span></span><span></span></div>
  <div class="foot"><span>© Copyright Halvora Trade Allies | All Rights Reserved</span><span>PAGE | 19</span></div>
</div>
<div class="slide" style="left:407px;top:2666px">
  <div class="t">Chart Slide</div>
  <div class="st">Subtitle Goes Here</div>
  <div class="mark">HTA</div>
  <div class="p" style="left:30px;top:42px;width:320px">Short placeholder line to describe the chart data shown below in a few words.</div>
  <svg style="position:absolute;left:14px;top:58px" width="350" height="130">
    <g font-family="Open Sans" font-size="3.6" fill="#999" text-anchor="end"><text x="12" y="12">100%</text><text x="12" y="40">75%</text><text x="12" y="68">50%</text><text x="12" y="96">25%</text><text x="12" y="122">0%</text></g>
    <g fill="#dedede">
      <rect x="26" y="10" width="14" height="110"/><rect x="62" y="10" width="14" height="110"/><rect x="98" y="10" width="14" height="110"/><rect x="134" y="10" width="14" height="110"/><rect x="170" y="10" width="14" height="110"/><rect x="206" y="10" width="14" height="110"/><rect x="242" y="10" width="14" height="110"/><rect x="278" y="10" width="14" height="110"/><rect x="314" y="10" width="14" height="110"/>
    </g>
    <rect x="26" y="95" width="14" height="25" fill="var(--navy)"/><rect x="62" y="60" width="14" height="60" fill="var(--navy)"/><rect x="98" y="72" width="14" height="48" fill="var(--green)"/>
    <rect x="134" y="84" width="14" height="36" fill="#bdbdbd"/><rect x="170" y="56" width="14" height="64" fill="var(--blue)"/><rect x="206" y="40" width="14" height="80" fill="#111"/>
    <rect x="242" y="72" width="14" height="48" fill="var(--navy)"/><rect x="278" y="24" width="14" height="96" fill="var(--navy)"/><rect x="314" y="42" width="14" height="78" fill="var(--green)"/>
    <g font-family="Open Sans" font-size="3.4" fill="#fff" text-anchor="middle"><text x="33" y="116">23%</text><text x="69" y="116">55%</text><text x="105" y="116">43%</text><text x="141" y="116">33%</text><text x="177" y="116">58%</text><text x="213" y="116">72%</text><text x="249" y="116">44%</text><text x="285" y="116">88%</text><text x="321" y="116">70%</text></g>
    <g font-family="Open Sans" font-size="3.6" fill="#999" text-anchor="middle"><text x="33" y="128">2012</text><text x="69" y="128">2013</text><text x="105" y="128">2014</text><text x="141" y="128">2015</text><text x="177" y="128">2016</text><text x="213" y="128">2017</text><text x="249" y="128">2018</text><text x="285" y="128">2019</text><text x="321" y="128">2020</text></g>
  </svg>
  <div class="foot"><span>© Copyright Halvora Trade Allies | All Rights Reserved</span><span>PAGE | 20</span></div>
</div>
<div class="slide" style="left:800px;top:2666px">
  <div class="t">Smart Art Slide</div>
  <div class="st">Subtitle Goes Here</div>
  <div class="mark">HTA</div>
  <svg style="position:absolute;left:0;top:0" width="376" height="212">
    <circle cx="188" cy="118" r="48" fill="none" stroke="#cfd9e8" stroke-width="6"/>
    <circle cx="188" cy="118" r="20" fill="var(--navy)"/>
    <circle cx="188" cy="70" r="16" fill="var(--navy)"/><circle cx="188" cy="166" r="16" fill="var(--navy)"/>
    <circle cx="140" cy="118" r="16" fill="var(--green)"/><circle cx="236" cy="118" r="16" fill="var(--green)"/>
    <g font-family="Open Sans" font-weight="600" font-size="4" fill="#fff" text-anchor="middle">
      <text x="188" y="119.5">Content Here</text><text x="188" y="69">Content</text><text x="188" y="74">Here</text>
      <text x="188" y="165">Content</text><text x="188" y="170">Here</text><text x="140" y="117">Content</text><text x="140" y="122">Here</text>
      <text x="236" y="117">Content</text><text x="236" y="122">Here</text>
    </g>
  </svg>
  <div class="p" style="left:212px;top:58px;width:80px">Get a clean and modern layout that is easy to edit</div>
  <div class="p" style="left:50px;top:112px;width:70px">Get a clean and modern layout that is easy to edit</div>
  <div class="p" style="left:262px;top:112px;width:70px">Get a clean and modern layout that is easy to edit</div>
  <div class="p" style="left:212px;top:162px;width:80px">Get a clean and modern layout that is easy to edit</div>
  <div class="foot"><span>© Copyright Halvora Trade Allies | All Rights Reserved</span><span>PAGE | 21</span></div>
</div>

<!-- row 8 -->
<div class="slide" style="left:14px;top:2904px">
  <div class="t">Table Chart Slide</div>
  <div class="st">Subtitle Goes Here</div>
  <div class="mark">HTA</div>
  <div class="ph" style="left:50px;top:62px;width:18px;height:108px;background:var(--navy);border-radius:2px"></div>
  <svg style="position:absolute;left:50px;top:62px" width="18" height="108"><g fill="none" stroke="#fff" stroke-width=".8"><circle cx="9" cy="14" r="3"/><rect x="6" y="31" width="6" height="6"/><path d="M6 56 l3 3 l4 -5"/><circle cx="9" cy="76" r="3"/><rect x="6" y="91" width="6" height="6"/></g></svg>
  <table class="tc" style="left:74px;top:58px;width:264px">
    <tr><th style="background:var(--navy)">TEXT HERE</th><th style="background:var(--blue)">TEXT HERE</th><th style="background:var(--green)">TEXT HERE</th></tr>
    <tr><td>Add Contents Title</td><td>Add Contents Title</td><td>Add Contents Title</td></tr>
    <tr><td>Modern Layout</td><td>Modern Layout</td><td>Modern Layout</td></tr>
    <tr><td>Add Contents Title</td><td>Add Contents Title</td><td>Add Contents Title</td></tr>
    <tr><td>Modern Layout</td><td>Modern Layout</td><td>Modern Layout</td></tr>
    <tr><td>Add Contents Title</td><td>Add Contents Title</td><td>Add Contents Title</td></tr>
  </table>
  <div class="foot"><span>© Copyright Halvora Trade Allies | All Rights Reserved</span><span>PAGE | 22</span></div>
</div>
<div class="slide" style="left:407px;top:2904px">
  <div class="t">Excel Slide</div>
  <div class="st">Subtitle Goes Here</div>
  <div class="mark">HTA</div>
  <svg style="position:absolute;left:20px;top:55px" width="130" height="130">
    <line x1="14" y1="10" x2="14" y2="110" stroke="#bbb" stroke-width=".6"/>
    <line x1="14" y1="110" x2="120" y2="120" stroke="#bbb" stroke-width=".6"/>
    <polygon points="14,70 50,50 90,60 120,45 120,75 90,88 50,78 14,95" fill="var(--navy)"/>
    <polygon points="14,95 50,78 90,88 120,75 120,90 90,100 50,95 14,108" fill="#2f9a6a"/>
    <polygon points="30,60 60,40 100,52 100,58 60,48 30,66" fill="var(--sky)"/>
    <g font-family="Open Sans" font-size="3.4" fill="#888"><text x="20" y="124">Category 1</text><text x="70" y="128">Category 2</text></g>
  </svg>
  <div class="sheet" style="left:150px;top:52px;width:210px">
    <span></span><span>Series 1</span><span>Series 2</span><span>Series 3</span><span></span><span></span><span></span><span></span>
    <span>Category 1</span><span>4.3</span><span>2.4</span><span>2</span><span></span><span></span><span></span><span></span>
    <span>Category 2</span><span>2.5</span><span>4.4</span><span>2</span><span></span><span></span><span></span><span></span>
    <span>Category 3</span><span>3.5</span><span>1.8</span><span>3</span><span></span><span></span><span></span><span></span>
    <span>Category 4</span><span>4.5</span><span>2.8</span><span>5</span><span></span><span></span><span></span><span></span>
    <span></span><span></span><span></span><span></span><span></span><span></span><span></span><span></span>
    <span></span><span></span><span></span><span></span><span></span><span></span><span></span><span></span>
    <span></span><span></span><span></span><span></span><span></span><span></span><span></span><span></span>
    <span></span><span></span><span></span><span></span><span></span><span></span><span></span><span></span>
    <span></span><span></span><span></span><span></span><span></span><span></span><span></span><span></span>
    <span></span><span></span><span></span><span></span><span></span><span></span><span></span><span></span>
    <span></span><span></span><span></span><span></span><span></span><span></span><span></span><span></span>
    <span></span><span></span><span></span><span></span><span></span><span></span><span></span><span></span>
    <span></span><span></span><span></span><span></span><span></span><span></span><span></span><span></span>
    <span></span><span></span><span></span><span></span><span></span><span></span><span></span><span></span>
    <span></span><span></span><span></span><span></span><span></span><span></span><span></span><span></span>
    <span></span><span></span><span></span><span></span><span></span><span></span><span></span><span></span>
  </div>
  <div class="foot"><span>© Copyright Halvora Trade Allies | All Rights Reserved</span><span>PAGE | 23</span></div>
</div>
<div class="slide" style="left:800px;top:2904px">
  <div class="t">Logo Slide</div>
  <div class="st">Subtitle Goes Here</div>
  <div class="mark">HTA</div>
  <div class="logo-box" style="left:22px;top:60px"></div><div class="logo-box" style="left:86px;top:60px"></div><div class="logo-box" style="left:150px;top:60px"></div><div class="logo-box" style="left:214px;top:60px"></div>
  <div class="logo-box" style="left:22px;top:96px"></div><div class="logo-box" style="left:86px;top:96px"></div><div class="logo-box" style="left:150px;top:96px"></div><div class="logo-box" style="left:214px;top:96px"></div>
  <div class="logo-box" style="left:22px;top:132px"></div><div class="logo-box" style="left:86px;top:132px"></div><div class="logo-box" style="left:150px;top:132px"></div>
  <div class="logo-box" style="left:214px;top:132px;border-style:dashed"></div>
  <div class="p" style="left:284px;top:82px;width:80px"><div class="h" style="font-size:4px">Content Here</div>Get a clean and modern presentation that is easy to change colors, photos and text.</div>
  <div class="foot"><span>© Copyright Halvora Trade Allies | All Rights Reserved</span><span>PAGE | 24</span></div>
</div>

<!-- row 9 -->
<div class="slide" style="left:14px;top:3142px">
  <div class="t">Editable Icons</div>
  <div class="mark">HTA</div>
  <div class="ph" role="img" aria-label="Grid of editable blue line icons for business topics" style="left:16px;top:40px;width:344px;height:148px;background:repeating-linear-gradient(90deg,#eef2f9 0 8px,#fff 8px 11px),linear-gradient(#fff,#fff);opacity:.9"></div>
  <div class="foot"><span></span><span>PAGE | 25</span></div>
</div>
<div class="slide" style="left:407px;top:3142px">
  <div class="t">Contact Us</div>
  <div class="faint" style="left:140px;top:40px;font-size:100px">HTA</div>
  <div class="ph" role="img" aria-label="Presenter portrait" style="left:38px;top:44px;width:40px;height:40px;border-radius:50%;background:linear-gradient(180deg,#d8d8d8,#777)"></div>
  <div style="position:absolute;left:24px;top:92px;width:86px;border:.6px solid #ccc;border-radius:6px;text-align:center;font:600 3.8px 'Open Sans',sans-serif;letter-spacing:1.2px;color:#777;padding:2px 0">PRESENTER NAME</div>
  <svg style="position:absolute;left:22px;top:108px" width="10" height="70"><g fill="var(--navy)"><rect x="2" y="2" width="5" height="7" rx="1"/><circle cx="4.5" cy="22" r="3"/><rect x="1" y="38" width="7" height="5"/><path d="M4.5 52 a3 3 0 0 1 3 3 c0 2 -3 5 -3 5 c0 0 -3 -3 -3 -5 a3 3 0 0 1 3 -3z"/></g></svg>
  <div class="p" style="left:36px;top:108px;line-height:4.1">+46 8 555 01 23<br>www.halvoratradeallies.se<br>hello@halvoratradeallies.se<br>Add your location here</div>
  <div class="brand" style="left:170px;width:150px;top:80px"><b style="font-size:20px">HTA</b><span style="font-size:7px">Halvora Trade Allies</span><i style="font-size:3.6px">Partners in lasting growth</i></div>
</div>
<div class="slide" style="left:800px;top:3142px">
  <div class="t">Additional color palette</div>
  <div class="mark">HTA</div>
  <div class="ph" style="left:38px;top:48px;width:138px;height:28px;background:linear-gradient(90deg,var(--navy),var(--blue))"></div>
  <div class="ph" style="left:196px;top:48px;width:138px;height:28px;background:linear-gradient(90deg,#7fc86a,#d8eec0)"></div>
  <div class="sw" style="left:38px;top:96px;background:var(--navy)"></div>
  <div class="sw" style="left:90px;top:96px;background:var(--blue)"></div>
  <div class="sw" style="left:142px;top:96px;background:var(--sky)"></div>
  <div class="sw" style="left:196px;top:96px;background:var(--green-light)"></div>
  <div class="sw" style="left:248px;top:96px;background:none"><svg width="34" height="28"><circle cx="17" cy="14" r="14" fill="#7ed03c"/></svg></div>
  <div class="sw" style="left:300px;top:96px;background:#2e6b45"></div>
  <div class="sw" style="left:38px;top:140px;background:#111"></div>
  <div class="sw" style="left:90px;top:140px;background:#8d8d8d"></div>
  <div class="sw" style="left:142px;top:140px;background:#d6d6d6"></div>
  <div class="sw" style="left:196px;top:140px;background:#3ccf9a"></div>
  <div class="sw" style="left:248px;top:140px;background:#a9efdc"></div>
  <div class="sw" style="left:300px;top:140px;background:#2c9a74"></div>
</div>

</div>
</body>
</html>
```